Real Estate Team Needs Business Cards

Double sided - Team Member on Front, Team Leader on Back (back side will contain more details).
Colors to use:
Red = R: 233 G: 1 B: 2
Grey = R: 89 G: 89 B: 89
Black= R: 0 B: 0 B: 0
** MAIN FOCUS ** ( separate border, color, design, etc. to really stand out - whatever you think draws the most attention ) on both sides for "Sell for 1%‡" and "Buy & receive up to a 1% rebate‡". Must have fine print **
**Please make both sides stand out and look unique / different
Business card to have round corners (standard size 3.5" x 2").:
Document Trim Size
89 x 51 mm
1050 x 600 pixels
Full Bleed Size
92 x 54 mm
1085 x 635 pixels
Basic example provided. Please redesign as you see best. In your design - Please use the same picture on both sides. Name, address, phone number, email, etc. will be provided to the selected design. QR code on back side only if there is room (not important)

```html
<!DOCTYPE html>
<html lang="en">
<head>
<meta charset="utf-8">
<title>Summit Harbor Realty – Business Cards</title>
<link href="https://fonts.googleapis.com/css2?family=Roboto:ital,wght@0,400;0,500;0,700;0,900;1,500;1,700&display=swap" rel="stylesheet">
<style>
  :root {
    --red: rgb(233, 1, 2);
    --grey: rgb(89, 89, 89);
    --black: #000;
    --white: #fff;
    --backdrop: #6b727c;
    --suit-blue: #2c4f8f;
    --photo-light: #e9edf3;
  }
  * { box-sizing: border-box; margin: 0; padding: 0; }
  html, body {
    width: 1200px; height: 900px; overflow: hidden;
    background: var(--backdrop);
    font-family: 'Roboto', sans-serif;
  }
  .sheet {
    width: 1200px; height: 900px;
    display: flex; flex-direction: column; align-items: center; justify-content: center;
    gap: 36px;
  }
  .card {
    position: relative;
    width: 700px; height: 400px;
    border-radius: 14px;
    overflow: hidden;
    box-shadow: 0 10px 28px rgba(0,0,0,.35);
  }

  /* ---------- Back side ---------- */
  .card--back { background: var(--black); color: var(--white); }
  .brand {
    display: flex; align-items: center; gap: 12px;
    font-weight: 900; text-transform: uppercase; letter-spacing: .02em;
  }
  .brand__mark { width: 18px; height: 18px; background: var(--red); flex: none; }
  .card--back .brand {
    position: absolute; left: 50%; top: 130px; transform: translateX(-50%);
    font-size: 38px; color: var(--white); white-space: nowrap;
  }
  .card--back .brand-rule {
    position: absolute; left: 140px; right: 140px; top: 188px;
    height: 3px; background: var(--red);
  }
  .offer-line {
    position: absolute; left: 0; right: 0; bottom: 58px;
    display: flex; justify-content: center; gap: 22px;
    font-size: 19px; font-weight: 500; text-transform: uppercase; letter-spacing: .02em;
  }
  .offer-line__item { display: flex; align-items: center; gap: 9px; }
  .bullet { width: 9px; height: 9px; background: var(--red); flex: none; }

  /* ---------- Front side ---------- */
  .card--front { background: var(--white); }
  .card--front .brand {
    position: absolute; left: 36px; top: 40px;
    font-size: 26px; color: var(--black);
  }
  .card--front .brand-rule {
    position: absolute; left: 36px; width: 330px; top: 80px;
    height: 2px; background: var(--red);
  }
  .agent { position: absolute; left: 36px; top: 112px; }
  .agent__name { color: var(--red); font-weight: 900; font-size: 32px; line-height: 1.1; }
  .agent__title { color: var(--black); font-size: 17px; margin-top: 2px; }
  .contact {
    position: absolute; left: 36px; top: 196px;
    list-style: none; color: var(--grey); font-size: 16px;
  }
  .contact li { display: flex; align-items: center; gap: 10px; height: 24px; }
  .contact svg { width: 15px; height: 15px; fill: var(--red); flex: none; }
  .offer-band {
    position: absolute; left: 0; bottom: 0; width: 420px; height: 92px;
    background: var(--black); border-top: 5px solid var(--red);
    padding: 16px 0 0 36px;
    color: var(--red); font-style: italic; font-weight: 700; font-size: 19px;
  }
  .offer-band li { list-style: none; display: flex; align-items: center; gap: 9px; height: 28px; }
  .portrait {
    position: absolute; right: 22px; bottom: 0; width: 290px; height: 300px;
    background: linear-gradient(180deg, var(--photo-light) 0%, var(--photo-light) 45%, var(--suit-blue) 100%);
    border-radius: 140px 140px 0 0;
  }
</style>
</head>
<body>
<main class="sheet">

  <section class="card card--back" aria-label="Business card back">
    <div class="brand"><span class="brand__mark"></span>Summit Harbor Realty</div>
    <div class="brand-rule"></div>
    <div class="offer-line">
      <span class="offer-line__item"><span class="bullet"></span>Sell for 1%*</span>
      <span class="offer-line__item"><span class="bullet"></span>Buy &amp; receive up to a 1% rebate*</span>
    </div>
  </section>

  <section class="card card--front" aria-label="Business card front">
    <div class="brand"><span class="brand__mark"></span>Summit Harbor Realty</div>
    <div class="brand-rule"></div>

    <div class="agent">
      <h1 class="agent__name">Daniel Brooks</h1>
      <p class="agent__title">President</p>
    </div>

    <ul class="contact">
      <li>
        <svg viewBox="0 0 24 24"><path d="M6.6 10.8a15.1 15.1 0 0 0 6.6 6.6l2.2-2.2a1 1 0 0 1 1-.25 11.4 11.4 0 0 0 3.6.57 1 1 0 0 1 1 1V20a1 1 0 0 1-1 1A17 17 0 0 1 3 4a1 1 0 0 1 1-1h3.5a1 1 0 0 1 1 1c0 1.25.2 2.45.57 3.6a1 1 0 0 1-.25 1z"/></svg>
        555-014-2286
      </li>
      <li>
        <svg viewBox="0 0 24 24"><path d="M7 1h10a2 2 0 0 1 2 2v18a2 2 0 0 1-2 2H7a2 2 0 0 1-2-2V3a2 2 0 0 1 2-2zm0 3v14h10V4z"/></svg>
        555-019-7341
      </li>
      <li>
        <svg viewBox="0 0 24 24"><path d="M2 5h20v14H2zm2 2v.4l8 5 8-5V7z"/></svg>
        brooks@summitharborrealty.com
      </li>
      <li>
        <svg viewBox="0 0 24 24"><path d="M12 2a10 10 0 1 0 0 20 10 10 0 0 0 0-20zm-1 17.9A8 8 0 0 1 4.2 10L9 14.8V16a2 2 0 0 0 2 2zm6.9-2.5A2 2 0 0 0 16 16h-1v-3a1 1 0 0 0-1-1H8v-2h2a1 1 0 0 0 1-1V7h2a2 2 0 0 0 2-2v-.4a8 8 0 0 1 2.9 12.8z"/></svg>
        www.summitharborrealty.com
      </li>
    </ul>

    <ul class="offer-band">
      <li><span class="bullet"></span>Sell for 1%*</li>
      <li><span class="bullet"></span>Buy &amp; receive up to a 1% rebate*</li>
    </ul>

    <div class="portrait" role="img" aria-label="Portrait photo of the agent in a navy suit and light blue tie"></div>
  </section>

</main>
</body>
</html>
```